Ridgeline Builders Guild Business card

We are looking for a new business card design with photo included.
Our business is a nonprofit construction contractor membership organization. We offer business education, assist with business setup and licensing, provide safety training, and provide a member directory.
URL: www.ridgelinebuildersguild.org
Color code:
CMYK: 0 cyan, 42 magenta, 100 yellow, 0 black for Print.
Hexidecimal: #FF9900
RGB: R 255; G 153; B 0

```html
<!DOCTYPE html>
<html lang="en">
<head>
<meta charset="utf-8">
<title>Ridgeline Builders Guild – Business Card</title>
<link href="https://fonts.googleapis.com/css2?family=Arimo:wght@400;700&display=swap" rel="stylesheet">
<style>
  :root {
    --orange: #ff9900;
    --edge: #d9850a;
    --ink: #1a1a1a;
    --text-grey: #6b6b6b;
    --rule-grey: #8a8a8a;
    --paper: #f7f7f7;
    --charcoal: #2c2c2c;
    --charcoal-mark: #4a4a4a;
    --backdrop: #e4e4e2;
  }
  * { margin: 0; padding: 0; box-sizing: border-box; }
  html, body {
    width: 1200px; height: 801px; overflow: hidden;
    background: var(--backdrop);
    font-family: "Arimo", Arial, sans-serif;
  }
  .stage {
    position: relative; width: 1200px; height: 801px;
    display: flex; align-items: center; justify-content: center; gap: 40px;
  }
  .card {
    position: relative; width: 540px; height: 309px;
    border-bottom: 4px solid var(--edge);
  }
  /* Front */
  .card-front { background: var(--paper); }
  .front-brand {
    position: absolute; left: 40px; top: 0; bottom: 0; width: 225px;
    display: flex; align-items: center;
  }
  .brand-name {
    font-weight: 700; font-size: 19px; color: var(--ink);
    text-transform: uppercase; letter-spacing: 0.5px; line-height: 1.2;
  }
  .front-divider {
    position: absolute; left: 275px; top: 54px; bottom: 54px;
    width: 1px; background: var(--rule-grey);
  }
  .front-details {
    position: absolute; left: 298px; top: 52px; right: 16px;
    color: var(--text-grey); font-size: 13px; line-height: 1.35;
  }
  .person-name { color: var(--orange); font-weight: 700; font-size: 20px; line-height: 1.1; }
  .person-title { font-size: 14px; margin-bottom: 12px; }
  .address { margin-bottom: 12px; }
  .contact-list { list-style: none; }
  .contact-item { display: flex; align-items: center; gap: 9px; margin-bottom: 5px; white-space: nowrap; }
  .contact-icon { width: 14px; height: 14px; flex: none; }
  .url-domain { color: var(--orange); }
  /* Back */
  .card-back {
    background: var(--charcoal);
    display: flex; align-items: center; justify-content: center;
  }
  .back-brand {
    font-weight: 700; font-size: 40px; color: var(--charcoal-mark);
    text-transform: uppercase; text-align: center; line-height: 1.1; letter-spacing: 1px;
  }
</style>
</head>
<body>
<main class="stage">
  <section class="card card-front" aria-label="Business card front">
    <div class="front-brand"><p class="brand-name">Ridgeline Builders Guild</p></div>
    <div class="front-divider"></div>
    <div class="front-details">
      <p class="person-name">Marcus Hale</p>
      <p class="person-title">Manager</p>
      <p class="address">Your address, city<br>state, ZIP 0000</p>
      <ul class="contact-list">
        <li class="contact-item">
          <svg class="contact-icon" viewBox="0 0 16 16" aria-hidden="true"><path fill="var(--orange)" d="M3.5 1.5l2.5 0 1 3.5-1.6 1.2a8 8 0 0 0 4.4 4.4L11 9l3.5 1v2.5c0 1-1 2-2 2A11 11 0 0 1 1.5 3.5c0-1 1-2 2-2z"/></svg>
          <span>555-018-4270</span>
        </li>
        <li class="contact-item">
          <svg class="contact-icon" viewBox="0 0 16 16" aria-hidden="true"><rect x="1" y="3" width="14" height="10" fill="var(--orange)"/><path d="M1 3l7 6 7-6" fill="none" stroke="#fff" stroke-width="1.3"/></svg>
          <span>hello@ridgelinemail.com</span>
        </li>
        <li class="contact-item">
          <svg class="contact-icon" viewBox="0 0 16 16" aria-hidden="true"><circle cx="8" cy="8" r="7" fill="var(--orange)"/><g fill="none" stroke="#fff" stroke-width="1"><ellipse cx="8" cy="8" rx="3" ry="6.5"/><path d="M1.5 8h13M2.5 5h11M2.5 11h11"/></g></svg>
          <span>www.<span class="url-domain">ridgelinebuildersguild</span>.org</span>
        </li>
      </ul>
    </div>
  </section>
  <section class="card card-back" aria-label="Business card back">
    <p class="back-brand">Ridgeline<br>Builders Guild</p>
  </section>
</main>
</body>
</html>
```